Retail Sign for Houseplant Campaign

Sign will measure 3 to 4 foot tall by 22.2inches and place on rolling racks of houseplants for a retail promotion in The Brickfield Yard. The theme of the promotion will be "New Year, New You!" Selling points which should be on the sign are Houseplants give you a taste of nature, Houseplants boost air quality inside your home, Indoor plants reduce anxiety, Indoor plants make you more productive, Houseplants improve your concentration and memory.
Updates

Target Market(s)

People who love plants

Industry/Entity Type

Horticulture/ retail

Colors
00AB8E
00BBA5
67D7C9
C6EFE9
E9F9F6
59FF00
82FF00
B8FF75
E3FFCB
F4FFEA
FFF300
FFF600
FEFA6F
FFFEC7
FFFEE8

Requirements
Must have
• Must feel energetic and encourage people to buy plants. Should include 1-2 photos and the selling points listed

```html
<!DOCTYPE html>
<html lang="en">
<head>
<meta charset="utf-8">
<title>New Year, New You! – Houseplant Retail Sign</title>
<link rel="stylesheet" href="https://fonts.googleapis.com/css2?family=Abel&family=Oleo+Script:wght@400&family=Montserrat:wght@400&display=swap">
<style>
  :root {
    --page-bg: #e9ebe8;
    --sign-white: #ffffff;
    --sign-black: #111111;
    --brand-green: #2b4633;
    --teal-1: #13b79c;
    --teal-2: #00bba5;
    --teal-3: #67d7c9;
    --teal-4: #c6efe9;
    --lime-1: #79c92f;
    --lime-2: #d2df1a;
    --lime-3: #ebcf10;
    --lime-4: #f3e40a;
    --headline-teal: #00a9ab;
    --headline-yellow: #f6ec12;
    --copy-white: #f2f2f2;
    --photo-light: #eef0ef;
    --photo-mid: #d9d6d0;
    --photo-dark: #9a9896;
  }

  * { margin: 0; padding: 0; box-sizing: border-box; }

  html, body {
    width: 1200px;
    height: 1000px;
    overflow: hidden;
    background: var(--page-bg);
  }

  .sign {
    position: absolute;
    left: 379px;
    top: 36px;
    width: 442px;
    height: 928px;
    display: flex;
    flex-direction: column;
    background: var(--sign-white);
    box-shadow: 0 6px 24px rgba(0, 0, 0, 0.12);
  }

  .color-band {
    display: flex;
    height: 24px;
    flex: none;
  }
  .color-band span { flex: 1; }
  .color-band--teal span:nth-child(1) { background: var(--teal-1); }
  .color-band--teal span:nth-child(2) { background: var(--teal-2); }
  .color-band--teal span:nth-child(3) { background: var(--teal-3); }
  .color-band--teal span:nth-child(4) { background: var(--teal-4); }
  .color-band--lime span:nth-child(1) { background: var(--lime-1); }
  .color-band--lime span:nth-child(2) { background: var(--lime-2); }
  .color-band--lime span:nth-child(3) { background: var(--lime-3); }
  .color-band--lime span:nth-child(4) { background: var(--lime-4); }

  .brand {
    height: 127px;
    flex: none;
    display: flex;
    align-items: center;
    justify-content: center;
    gap: 14px;
    color: var(--brand-green);
    font-family: "Montserrat", sans-serif;
    font-weight: 400;
  }
  .brand__square {
    width: 54px;
    height: 54px;
    background: var(--brand-green);
  }
  .brand__name {
    display: flex;
    flex-direction: column;
    line-height: 1;
  }
  .brand__name-main {
    font-size: 38px;
    letter-spacing: 0.5px;
  }
  .brand__name-sub {
    font-size: 12px;
    letter-spacing: 12px;
    margin-top: 6px;
  }

  .hero-photo {
    height: 442px;
    flex: none;
    background: linear-gradient(180deg, var(--photo-light) 0%, var(--photo-mid) 60%, var(--photo-dark) 100%);
  }

  .message {
    flex: 1;
    background: var(--sign-black);
    padding: 30px 20px 0;
  }
  .headline {
    font-family: "Oleo Script", cursive;
    font-weight: 400;
    font-size: 54px;
    line-height: 56px;
  }
  .headline__line { display: block; white-space: nowrap; }
  .headline__line--first {
    color: var(--headline-teal);
    padding-left: 26px;
  }
  .headline__line--second {
    color: var(--headline-yellow);
    padding-left: 90px;
  }

  .selling-points {
    list-style: none;
    margin-top: 28px;
    text-align: center;
    font-family: "Abel", sans-serif;
    font-size: 18.5px;
    line-height: 22px;
    color: var(--copy-white);
  }
</style>
</head>
<body>
  <main class="sign">
    <div class="color-band color-band--teal">
      <span></span><span></span><span></span><span></span>
    </div>

    <header class="brand">
      <div class="brand__square"></div>
      <div class="brand__name">
        <span class="brand__name-main">VERDANT</span>
        <span class="brand__name-sub">HABITS</span>
      </div>
    </header>

    <div class="hero-photo" role="img" aria-label="Photo of a smiling woman placing a potted houseplant in a woven basket onto a white shelf in a bright living room"></div>

    <section class="message">
      <h1 class="headline">
        <span class="headline__line headline__line--first">"New Year,</span>
        <span class="headline__line headline__line--second">New You!"</span>
      </h1>
      <ul class="selling-points">
        <li>Houseplants give you a taste of nature.</li>
        <li>Houseplants boost air quality inside your home.</li>
        <li>Indoor plants reduce anxiety.</li>
        <li>Indoor plants make you more productive.</li>
        <li>Houseplants improve your concentration and memory.</li>
      </ul>
    </section>

    <div class="color-band color-band--lime">
      <span></span><span></span><span></span><span></span>
    </div>
  </main>
</body>
</html>
```